menu for prepared meals company

Currently have a menu set up with company logo, would like something more eye catching and artistic to make it look professional. This is a fitness and health driven company in regards to purchasing prepared meals to use towards fitness goals. Do not necessarily want the menu to be geared towards muscular men and women. Looking to have the menu be simple to understand, exactly what it stands for, and geared towards a large demographic in health and life style eating changes.

Target Market(s)

health/fitness

Industry/Entity Type

It Company

Requirements
Must have
• *please see set up for mock menu and apply changes that were applied in the word document menu information.
• ex:do not offer sweet potato and chicken hash*

```html
<!DOCTYPE html>
<html lang="en">
<head>
<meta charset="utf-8">
<title>Fit Plate Kitchen Menu</title>
<link href="https://fonts.googleapis.com/css2?family=Fredoka:wght@600&family=Quicksand:wght@400;500&display=swap" rel="stylesheet">
<style>
  :root {
    --red: #ee3a37;
    --red-text: #e8322f;
    --ink: #2b2b2b;
    --peach: #fde0b8;
    --white: #ffffff;
  }
  * { margin: 0; padding: 0; box-sizing: border-box; }
  html, body { width: 934px; height: 1200px; overflow: hidden; background: var(--white); }
  .menu { position: relative; width: 934px; height: 1200px; font-family: "Quicksand", sans-serif; color: var(--ink); }

  .top-band { position: absolute; top: 0; height: 101px; background: var(--red); }
  .top-band.left { left: 0; width: 340px; }
  .top-band.right { left: 595px; width: 339px; }

  .brand-box {
    position: absolute; left: 349px; top: -2px; width: 237px; height: 184px;
    border: 1.5px dashed var(--red); border-top: none; border-radius: 0 0 8px 8px;
    display: flex; align-items: center; justify-content: center; gap: 8px;
  }
  .brand-dot { width: 12px; height: 12px; border-radius: 50%; background: var(--red); }
  .brand-name { font-family: "Fredoka", sans-serif; font-weight: 600; font-size: 25px; color: var(--red); line-height: 1; }

  .heading { font-family: "Fredoka", sans-serif; font-weight: 600; color: var(--red); text-transform: uppercase; line-height: 1.4; }

  .specialty { position: absolute; left: 68px; top: 212px; width: 530px; }
  .specialty .heading { font-size: 35px; line-height: 1.2; }
  .specialty .price-note { color: var(--red-text); font-size: 16px; margin-top: 4px; }
  .specialty .items { margin-top: 18px; font-size: 15.5px; line-height: 20px; }
  .specialty .items p { margin-bottom: 5px; }
  .specialty .items p.tight { margin-bottom: 0; }

  .photo { position: absolute; }
  .photo.pasta { left: 642px; top: 222px; width: 216px; height: 220px; background: radial-gradient(circle at 55% 40%, #c9371f 0%, #b33019 35%, #e8c36a 65%, #f4f1ea 85%, #5a3d2b 100%); }
  .photo.protein { left: 61px; top: 668px; width: 304px; height: 166px; background: radial-gradient(ellipse at 50% 55%, #d8b58a 0%, #e8d7c0 50%, #ffffff 85%); }
  .photo.carb { left: 376px; top: 672px; width: 240px; height: 148px; background: radial-gradient(ellipse at 50% 55%, #b9824a 0%, #dcb98a 50%, #ffffff 85%); }
  .photo.veg { left: 636px; top: 672px; width: 232px; height: 152px; background: radial-gradient(ellipse at 50% 55%, #6a9a3a 0%, #d9543a 40%, #f2d27a 60%, #ffffff 85%); }

  .banner { position: absolute; left: 70px; top: 472px; width: 786px; height: 60px; }
  .banner svg { position: absolute; inset: 0; }
  .banner .banner-text {
    position: absolute; inset: 0; display: flex; align-items: center; justify-content: center;
    font-family: "Fredoka", sans-serif; font-weight: 600; font-size: 34px; color: var(--white);
  }

  .col-title { position: absolute; width: 260px; text-align: center; font-size: 35px; line-height: 48px; }
  .col-title.protein { left: 83px; top: 562px; }
  .col-title.carb { left: 364px; top: 554px; }
  .col-title.veg { left: 624px; top: 554px; }

  .size-header { position: absolute; left: 202px; top: 846px; font-size: 12px; }
  .protein-list { position: absolute; left: 69px; top: 864px; font-size: 17px; }
  .protein-list .row { position: relative; height: 25.8px; line-height: 25.8px; width: 300px; }
  .protein-list .price { position: absolute; color: var(--red-text); }
  .protein-list .half { left: 145px; }
  .protein-list .full { left: 233px; }

  .choice-list { position: absolute; width: 240px; text-align: center; font-size: 17px; line-height: 25.8px; }
  .choice-list.carb { left: 374px; top: 865px; }
  .choice-list.veg { left: 634px; top: 862px; }

  .portion-note { position: absolute; left: 430px; top: 976px; width: 380px; text-align: center; font-size: 11.5px; line-height: 14.5px; }

  .extras {
    position: absolute; left: 402px; top: 1044px; width: 456px; height: 87px; background: var(--peach);
    display: flex; flex-direction: column; justify-content: center; align-items: center;
    font-size: 16px; line-height: 25px; text-align: center;
  }
</style>
</head>
<body>
<div class="menu">
  <div class="top-band left"></div>
  <div class="top-band right"></div>
  <div class="brand-box">
    <span class="brand-dot"></span>
    <span class="brand-name">Fit Plate Kitchen</span>
  </div>

  <section class="specialty">
    <h1 class="heading">Specialty Meals</h1>
    <p class="price-note">All specialty Meals are $9.95</p>
    <div class="items">
      <p>Pasta with Turkey Meatballs- Whole grain pasta with turkey meatballs and a tomato sauce</p>
      <p class="tight">Stir fry- Chicken, stir fry vegetable mix with jasmine rice</p>
      <p>Turkey burger- Turkey Patty on a multigrain flat bread with side of sweet potato fries</p>
      <p>Stuffed Pepper -Pepper stuffed with ground turkey, your choice of whole grain or jasmine rice combined in a red sauce</p>
    </div>
  </section>
  <div class="photo pasta" role="img" aria-label="Plate of spaghetti with turkey meatballs in tomato sauce"></div>

  <div class="banner">
    <svg width="786" height="60" viewBox="0 0 786 60">
      <polygon points="0,0 786,0 758,30 786,60 0,60 28,30" fill="var(--red)"/>
      <polyline points="6,5 780,5 754,30 780,55 6,55 32,30 6,5" fill="none" stroke="#ffffff" stroke-width="1" stroke-dasharray="3 3"/>
    </svg>
    <div class="banner-text">CREATE YOUR OWN</div>
  </div>

  <h2 class="heading col-title protein">Choose<br>Protein</h2>
  <h2 class="heading col-title carb">Carb<br>Choices</h2>
  <h2 class="heading col-title veg">Vegetable<br>Choices</h2>

  <div class="photo protein" role="img" aria-label="Assorted protein foods: meat, fish, eggs, cheese, beans and nuts"></div>
  <div class="photo carb" role="img" aria-label="Assorted carbohydrates: bread, pasta, grains and rice"></div>
  <div class="photo veg" role="img" aria-label="Assorted fresh vegetables"></div>

  <p class="size-header">Half size=4oz | Full size=8oz</p>
  <div class="protein-list">
    <div class="row">Chicken<span class="price half">$7.95</span><span class="price full">$8.95</span></div>
    <div class="row">Ground Beef<span class="price half">$7.95</span><span class="price full">$8.95</span></div>
    <div class="row">Ground Turkey<span class="price half">$7.95</span><span class="price full">$8.95</span></div>
    <div class="row">Steak<span class="price half">$9.95</span><span class="price full">$10.95</span></div>
    <div class="row">Turkey Tenderloin<span class="price half">$7.95</span><span class="price full">$8.95</span></div>
    <div class="row">Salmon<span class="price full">$11.95</span></div>
    <div class="row">Tilapia<span class="price full">$10.95</span></div>
    <div class="row">Cod<span class="price full">$9.95</span></div>
    <div class="row">Veggie Burger<span class="price full">$9.95</span></div>
  </div>

  <div class="choice-list carb">
    Whole Grain Pasta<br>Whole Grain Rice<br>Jasmine Rice<br>Sweet potato
  </div>
  <div class="choice-list veg">
    Whole Grain Pasta<br>Whole Grain Rice<br>Jasmine Rice<br>Sweet potato
  </div>

  <p class="portion-note">Half Size= 1/2 cup Full Size = 1cup<br>If two vegetable options are wanted they may choose<br>two for low carb meal combo.</p>

  <div class="extras">
    <p>Also offer gluten free pasta as a carb option*</p>
    <p>At home or delivery within 20 miles for small fee.</p>
  </div>
</div>
</body>
</html>
```